Excavation Service Truck Design

I have attached a few examples of the look/feel we would like to have with our design. Prefer an electric blue with lime green and silver accents for graphics to make it pop. We prefer a clean logo that is not too busy. Varlo Excavation is the company name. The last photo is the truck we will be putting the graphics on.

Font styles to use
Other font styles liked:
• All uppercase font with a border and shadow

Colors
0054AA
0677BA
7BADD7
CADEEF
E8F1F8
0094D4
00A9DD
6FCCEA
C7EBF8
E9F6FB
59FF00
82FF00
B8FF75
E3FFCB
F4FFEA

```html
<!DOCTYPE html>
<html lang="en">
<head>
<meta charset="utf-8">
<title>Varlo Excavation – Service Body Graphics</title>
<link href="https://fonts.googleapis.com/css2?family=Montserrat:wght@500;600;700&display=swap" rel="stylesheet">
<style>
  :root{
    --canvas:#eef0f2;
    --body-black:#141210;
    --plate-silver:#c9ccd0;
    --electric-blue:#1a3cff;
    --outline:#dfe6ff;
    --lime:#3fe61a;
    --phone-lime:#59ff00;
    --white:#ffffff;
    --arch-edge:#3a3836;
    --sky-blue:#6fccea;
  }
  html,body{margin:0;padding:0;width:1200px;height:1200px;overflow:hidden;background:var(--canvas);}
  .canvas{position:relative;width:1200px;height:1200px;}
  .service-panel{
    position:absolute;left:40px;top:394px;width:1120px;height:412px;
    background:var(--body-black);overflow:hidden;
    font-family:'Montserrat',sans-serif;
  }
  .tread-plate{position:absolute;left:0;top:0;width:100%;height:16px;
    background:linear-gradient(180deg,#e4e6e9,var(--plate-silver));}
  .company-name{
    position:absolute;left:28px;top:26px;margin:0;
    font-weight:700;font-size:120px;line-height:1;letter-spacing:0;
    color:var(--electric-blue);white-space:nowrap;
    text-shadow:
      1.5px 0 0 var(--outline), -1.5px 0 0 var(--outline),
      0 1.5px 0 var(--outline), 0 -1.5px 0 var(--outline),
      1px 1px 0 var(--outline), -1px -1px 0 var(--outline),
      1px -1px 0 var(--outline), -1px 1px 0 var(--outline),
      4px 4px 2px rgba(0,0,0,.6);
  }
  .accent-rule{position:absolute;left:33px;top:152px;height:11px;}
  .accent-rule.blue{width:611px;background:var(--electric-blue);}
  .accent-rule.green{left:644px;width:476px;background:var(--lime);}
  .brand-tile{
    position:absolute;left:0;top:189px;width:246px;height:206px;box-sizing:border-box;
    background:var(--white);border:4px solid var(--electric-blue);border-left:none;
    border-top-right-radius:120px;
    display:flex;flex-direction:column;align-items:center;justify-content:center;gap:10px;
  }
  .brand-dot{width:46px;height:46px;border-radius:50%;background:var(--sky-blue);}
  .brand-name{font-weight:700;font-size:24px;line-height:1.1;color:var(--electric-blue);text-align:center;}
  .phone{position:absolute;left:363px;top:176px;margin:0;font-weight:700;font-size:40px;color:var(--phone-lime);letter-spacing:1px;}
  .website{position:absolute;left:363px;top:224px;margin:0;font-weight:600;font-size:29px;color:var(--white);}
  .side-rule{position:absolute;left:919px;top:204px;width:201px;height:11px;background:var(--electric-blue);}
  .services{position:absolute;left:919px;top:248px;margin:0;padding:0;list-style:none;
    font-weight:500;font-size:30px;line-height:1.12;color:var(--white);}
  .wheel-arch{position:absolute;left:380px;top:270px;width:430px;height:142px;}
</style>
</head>
<body>
<div class="canvas">
  <section class="service-panel">
    <div class="tread-plate"></div>
    <h1 class="company-name">Varlo Excavation</h1>
    <div class="accent-rule blue"></div>
    <div class="accent-rule green"></div>
    <div class="brand-tile">
      <div class="brand-dot"></div>
      <div class="brand-name">Varlo<br>Excavation</div>
    </div>
    <p class="phone">123-456-7890</p>
    <p class="website">VARLO EXCAVATION.COM</p>
    <div class="side-rule"></div>
    <ul class="services">
      <li>SEPTIC</li>
      <li>UTILITIES</li>
      <li>SITEWORK</li>
    </ul>
    <svg class="wheel-arch" viewBox="0 0 430 142" aria-hidden="true">
      <path d="M4 142 V70 Q4 8 70 8 H360 Q426 8 426 70 V142 Z" fill="var(--canvas)" stroke="var(--arch-edge)" stroke-width="6"/>
    </svg>
  </section>
</div>
</body>
</html>
```